High Quality fast food restaurant - Quonfel

Quonfel is a fast food company with its target's focused on logistic, simplicity, high quality, freshness and modern.

We need a web design where the customers can get a complete idea of our high quality completeness, we want to take fast food to a new upper level.

We would like to see the colours of wood and metal. Pictures have been attached of our local.

We would like to have something in similar to: http://www.zq-vorn.com/
Updates

Images for the food we are going to sell can be found here: http://trq.lk/uRTWQ

It will be the images with rice, french fries or pita bread.

Target Market(s)

The fast food eating people between sloppy food and restaurant level.

Industry/Entity Type

Fast Food Restaurant

Requirements
Should not have
• No Flash or Java

```html
<!DOCTYPE html>
<html lang="en">
<head>
<meta charset="utf-8">
<title>Quonfel — Contact Us</title>
<link rel="stylesheet" href="https://fonts.googleapis.com/css2?family=Marcellus&family=Arimo:wght@400;700&display=swap">
<style>
  :root {
    --wood-dark: #2b160d;
    --wood-mid: #4a2a1a;
    --wood-light: #5c3522;
    --teal: #1a7f76;
    --panel: #3d2115;
    --field: #58331f;
    --ink: #3a2214;
    --cream: #fdf1d2;
    --white: #ffffff;
    --black: #111111;
  }
  * { box-sizing: border-box; margin: 0; padding: 0; }
  html, body { width: 1200px; height: 1000px; overflow: hidden; background: var(--white); }
  .page { position: relative; width: 1200px; height: 1000px; overflow: hidden; font-family: "Arimo", Arial, sans-serif; }

  .wood {
    background:
      repeating-linear-gradient(180deg, rgba(0,0,0,0.18) 0 1px, transparent 1px 14px),
      linear-gradient(180deg, var(--wood-dark) 0%, var(--wood-mid) 55%, var(--wood-dark) 100%);
  }

  .site-header { position: absolute; left: 0; top: 0; width: 1200px; height: 118px; }
  .brand {
    position: absolute; left: 157px; top: 36px;
    font-family: "Marcellus", serif; font-size: 36px; color: var(--white); letter-spacing: 1px;
  }
  .main-nav a {
    position: absolute; top: 94px; font-family: "Marcellus", serif; font-size: 13px;
    letter-spacing: 1.2px; color: var(--white); text-decoration: none;
  }
  .main-nav .is-active {
    top: 0; left: 903px; width: 100px; height: 125px; background: var(--teal);
    padding-top: 94px; text-align: center;
  }

  .hero {
    position: absolute; left: 0; top: 118px; width: 1200px; height: 530px;
    background:
      radial-gradient(ellipse at 22% 20%, #f3e7b8 0%, transparent 45%),
      radial-gradient(ellipse at 75% 55%, #e4dcb0 0%, transparent 55%),
      linear-gradient(100deg, #f7ecd6 0%, #fbf2d9 40%, #efe9c4 70%, #f7f0cd 100%);
  }
  .hero-title {
    position: absolute; left: 153px; top: 150px;
    font-family: "Marcellus", serif; font-size: 29px; font-weight: 400; color: var(--ink);
  }
  .hero-intro {
    position: absolute; left: 156px; top: 196px; font-size: 15.5px; line-height: 18px; color: var(--ink);
  }

  .contact-form {
    position: absolute; left: 154px; top: 247px; width: 485px; height: 383px; background: var(--panel);
  }
  .contact-form h2 {
    position: absolute; left: 5px; top: 18px; font-size: 18px; font-weight: 400; color: #efdcc6;
  }
  .contact-form label { position: absolute; left: 16px; font-size: 14px; color: var(--white); }
  .contact-form .field { position: absolute; left: 119px; width: 240px; height: 33px; background: var(--field); border: 0; }
  .contact-form .field-area { width: 345px; height: 129px; }
  .submit {
    position: absolute; left: 337px; top: 343px; width: 126px; height: 33px;
    background: var(--teal); color: var(--white); border: 0; font-family: inherit; font-size: 14px;
  }

  .menu-band { position: absolute; left: 0; top: 648px; width: 1200px; height: 160px; }
  .dish { position: absolute; top: 675px; width: 175px; height: 175px; border-radius: 50%; }
  .price {
    position: absolute; top: 694px; width: 47px; height: 47px; border-radius: 50%;
    background: var(--teal); color: var(--white); font-family: "Marcellus", serif; font-size: 11px;
    display: flex; align-items: center; justify-content: center;
  }

  .menu-intro h3 { position: absolute; left: 174px; top: 871px; font-size: 16px; font-weight: 400; color: var(--black); }
  .menu-intro p {
    position: absolute; left: 172px; top: 897px; width: 866px; text-align: center;
    font-size: 13px; line-height: 15px; color: var(--black);
  }

  .footer-nav a {
    position: absolute; top: 984px; font-size: 10px; font-weight: 700; color: var(--black); text-decoration: none;
  }
  .social { position: absolute; top: 978px; width: 18px; height: 18px; border-radius: 50%; background: var(--black); }
</style>
</head>
<body>
<div class="page">

  <header class="site-header wood">
    <div class="brand">QUONFEL</div>
    <nav class="main-nav">
      <a href="#" style="left:526px">HOME</a>
      <a href="#" style="left:599px">MENU</a>
      <a href="#" style="left:674px">FRESH OFFERS</a>
      <a href="#" style="left:806px">LOCATION</a>
      <a href="#" class="is-active">CONTACT US</a>
    </nav>
  </header>

  <section class="hero" role="img" aria-label="Soft photo of a stuffed pita sandwich with tomatoes, chips and a bowl of soup"></section>

  <h1 class="hero-title">Something to say ? Get in touch with us !</h1>
  <p class="hero-intro">We love to know your opinion about us - good or bad !<br>Please fill in the form below and we’ll get back to you soon !</p>

  <form class="contact-form">
    <h2>CONTACT FORM</h2>
    <label style="top:64px">Full name *</label>
    <input class="field" style="top:60px" type="text">
    <label style="top:114px">Email *</label>
    <input class="field" style="top:106px" type="email">
    <label style="top:162px">Subject *</label>
    <input class="field" style="top:152px" type="text">
    <label style="top:210px">Comment *</label>
    <textarea class="field field-area" style="top:199px"></textarea>
    <button class="submit" type="button">Submit Form</button>
  </form>

  <section class="menu-band wood"></section>

  <div class="dish" style="left:154px;background:radial-gradient(circle at 45% 55%,#e9d8b8,#b7773f 60%,#4a2b1a)" role="img" aria-label="Wrap with chicken and french fries"></div>
  <div class="dish" style="left:392px;background:radial-gradient(circle at 50% 55%,#cfae82,#8a6a3e 55%,#2f4b2a)" role="img" aria-label="Stuffed pita bread on a plate"></div>
  <div class="dish" style="left:632px;background:radial-gradient(circle at 50% 55%,#f3eee6,#c98a52 55%,#51602e)" role="img" aria-label="Falafel wrap with vegetables"></div>
  <div class="dish" style="left:879px;background:radial-gradient(circle at 50% 55%,#e2b683,#a2502f 55%,#f0d8d4)" role="img" aria-label="Grilled meat pita with salad"></div>

  <div class="price" style="left:136px">$ 32.99</div>
  <div class="price" style="left:377px">$ 22.99</div>
  <div class="price" style="left:614px">$ 40.99</div>
  <div class="price" style="left:860px">$ 20.99</div>

  <section class="menu-intro">
    <h3>MENU</h3>
    <p>Lorem ipsum dolor sit amet, consectetur adipisicing elit, sed do eiusmod tempor incididunt ut labore et dolore magna aliqua. Ut enim ad minim veniam, quis nostrud exercitation ullamco laboris nisi ut aliquip ex ea commodo consequat.Duis aute irure dolor in reprehenderit in voluptate velit esse cillum dolore eu fugiat nulla pariatur. Excepteur sint occaecat cupidatat non proident</p>
  </section>

  <nav class="footer-nav">
    <a href="#" style="left:174px">HOME</a>
    <a href="#" style="left:228px">MENU</a>
    <a href="#" style="left:283px">FRESH OFFERS</a>
    <a href="#" style="left:381px">LOCATION</a>
    <a href="#" style="left:455px">CONTACT US</a>
  </nav>

  <span class="social" style="left:938px" aria-label="Social link"></span>
  <span class="social" style="left:972px" aria-label="Social link"></span>
  <span class="social" style="left:1011px" aria-label="Social link"></span>

</div>
</body>
</html>
```